Website for virtual assistant and proofreader

Professional, feminine (but not flowery!) website offering and explaining my services as a VA and Proofreader. Probably only 7 pages: home, about, services (x2), fees, testimonials and contact page. <br/><br/>I already have most of the content, which I have uploaded so you can get an idea of waht I do. I have brand colours and logo already also uploaded. I really just need the bones of the site to be designed and am happy/capable of setting this up as a Wordpress site. I'm just rubbish at design!

Industry/Entity Type

Business Service

Coding

Coded - Design and coding required

Number of Pages Required

4 page

Other font styles liked:
• Roboto Bold + Great Vibes

Colors
3276b5
fee3d4

Requirements
Must have
• should be informative, professional, feminine. Clean, clear, CTA's links to services and fees pages
• Also, see all 3 colour codes on the attached doc.
Nice to have
• business images but place holders will do
Should not have
• Nothing flowery or cartoons! Not 'busy'

```html
<!DOCTYPE html>
<html lang="en">
<head>
<meta charset="utf-8">
<title>Maren T Holloway – Virtual Assistant and Proofreader</title>
<link href="https://fonts.googleapis.com/css2?family=Lato:wght@400;700;900&family=Lobster+Two:ital,wght@1,700&display=swap" rel="stylesheet">
<style>
:root{
  --blue:#1e4e79;
  --peach:#efb9a5;
  --taupe:#7b6f6c;
  --ink:#333333;
  --muted:#555555;
  --white:#ffffff;
  --footer:#2b2b2b;
  --rule:#d8d8d8;
}
*{box-sizing:border-box;margin:0;padding:0}
html,body{width:1200px;height:4064px;overflow:hidden}
body{position:relative;font-family:'Lato',sans-serif;color:var(--ink);background:var(--white)}
.abs{position:absolute}
.center{text-align:center;left:0;width:1200px}
.btn{position:absolute;background:var(--peach);color:#2a2a2a;font-weight:700;display:flex;align-items:center;justify-content:center}
.btn-lg{width:208px;height:58px;font-size:22px}
.btn-sm{width:160px;height:44px;font-size:16px}
.script{font-family:'Lobster Two',cursive;font-style:italic;font-weight:700}

/* header */
.site-header{top:0;left:0;width:1200px;height:134px;background:var(--white)}
.brand{left:76px;top:46px;display:flex;align-items:center;gap:10px}
.brand-mark{width:26px;height:26px;border-radius:50%;background:var(--blue)}
.brand-name{font-size:19px;font-weight:700;color:var(--blue);line-height:1.1}
.brand-tag{font-size:10px;color:var(--ink);margin-top:3px}
.main-nav{top:63px;right:74px;display:flex;gap:34px;font-size:15px;font-weight:700;color:#222}
.main-nav .active{color:var(--blue)}

/* hero */
.hero{top:134px;left:0;width:1200px;height:631px;background:linear-gradient(120deg,#8a5a34 0%,#b98654 35%,#d9c7ac 55%,#6f4a2c 100%)}
.hero-title{top:330px;font-size:82px;color:var(--white);text-shadow:0 2px 6px rgba(0,0,0,.35)}
.hero-sub{top:428px;font-size:32px;color:var(--white);text-shadow:0 2px 6px rgba(0,0,0,.45)}

/* welcome */
.section-title{font-size:29px;font-weight:900;color:var(--blue)}
.welcome-title{top:834px}
.welcome-text{top:892px;left:90px;width:1020px;font-size:14.5px;line-height:27.5px;text-align:center}

/* services */
.services{top:1167px;left:0;width:1200px;height:746px;background:var(--taupe)}
.services-title{top:1230px;font-size:28px;font-weight:900;color:var(--white)}
.services-text{top:1283px;left:74px;width:1052px;font-size:14.5px;line-height:27.5px;color:var(--white);text-align:center}
.card{position:absolute;width:513px;height:208px;background:var(--white);border-radius:3px}
.card-icon{position:absolute;left:30px;top:30px;width:52px;height:52px}
.card-title{position:absolute;left:100px;top:28px;font-size:18.5px;font-weight:700;color:var(--blue)}
.card-text{position:absolute;left:100px;top:59px;width:340px;font-size:14px;line-height:25px;color:var(--ink)}

/* quote */
.tagline{top:1968px;font-size:44px;line-height:52px;color:var(--blue)}

/* why me */
.why{top:2145px;left:0;width:613px;height:386px;background:var(--taupe)}
.why-photo{top:2145px;left:613px;width:587px;height:386px;background:linear-gradient(135deg,#b9874f 0%,#d8ab76 45%,#8f5a3a 100%)}
.why-title{top:2240px;left:74px;font-size:27px;font-weight:900;color:var(--white)}
.why-text{top:2293px;left:74px;width:520px;font-size:14px;line-height:27.5px;color:var(--white)}
.caption-name{top:2438px;left:631px;font-size:26px;color:#222}
.caption-role{top:2474px;left:662px;font-size:18px;font-weight:700;color:#222}

/* stories */
.story-photo{position:absolute;top:2607px;width:513px;height:252px}
.story-title{position:absolute;top:2880px;font-size:22.5px;font-weight:700;color:var(--blue)}
.story-text{position:absolute;top:2916px;width:513px;font-size:14px;line-height:27px;color:var(--ink)}
.load-more{position:absolute;display:flex;align-items:center;gap:16px;font-size:14px;font-weight:700;color:#e39a80}
.load-more span.rule{flex:1;height:1px;background:var(--rule)}

/* calling */
.calling-photo{top:3118px;left:0;width:587px;height:386px;background:linear-gradient(110deg,#c7c3bd 0%,#e9e2d6 50%,#a59a8d 100%)}
.calling{top:3118px;left:587px;width:613px;height:386px;background:var(--taupe)}
.calling-title{top:3174px;left:613px;font-size:28px;line-height:34px;font-weight:900;color:var(--white)}
.calling-text{top:3260px;left:613px;width:520px;font-size:14px;line-height:27.5px;color:var(--white)}

/* testimonials */
.testi-title{top:3561px}
.testi{position:absolute;top:3628px;width:320px;text-align:center}
.testi-mark{font-family:Georgia,serif;font-size:56px;line-height:40px;font-weight:700;color:#eaa690;height:36px}
.testi-text{margin-top:12px;font-size:14.5px;line-height:27.5px;color:var(--ink)}
.testi-name{margin-top:12px;font-size:16px;font-weight:700;color:var(--blue)}

/* footer */
.site-footer{top:3880px;left:0;width:1200px;height:184px;background:var(--footer)}
.footer-nav{top:3924px;display:flex;justify-content:center;gap:36px;font-size:15px;font-weight:700;color:var(--white)}
.copyright{top:3961px;font-size:12.5px;color:#cfcfcf}
.social{top:3992px;display:flex;justify-content:center;gap:24px}
.social span{width:22px;height:22px;border-radius:50%;background:var(--white)}
</style>
</head>
<body>

<header class="abs site-header">
  <div class="abs brand">
    <span class="brand-mark"></span>
    <div>
      <div class="brand-name">Maren T Holloway</div>
      <div class="brand-tag">Virtual Assistant and Proofreader</div>
    </div>
  </div>
  <nav class="abs main-nav">
    <span class="active">HOME</span><span>ABOUT</span><span>SERVICES</span><span>FEES</span><span>TESTIMONIALS</span><span>CONTACT</span>
  </nav>
</header>

<section class="abs hero" role="img" aria-label="Photo of hands holding an open book and a coffee mug on a wooden desk"></section>
<div class="abs center hero-title script">Allow me...</div>
<div class="abs center hero-sub">to handle the details so you can get on with business.</div>
<a class="btn btn-lg" style="left:379px;top:500px">Learn More</a>
<a class="btn btn-lg" style="left:613px;top:500px">Contact Us</a>

<h2 class="abs center section-title welcome-title">WELCOME TO MAREN</h2>
<p class="abs welcome-text">Every great leader is backed by diligent and knowledgeable support. Have you ever wondered what it would be like to have your very own personal assistant? Well, you can. A virtual assistant can do everything a full-time assistant can, with the added bonus that she can save you money.<br>Whether you need daily help, or help with special assignments or big projects, hiring me as your VA will save you the costs typically associated with an employee--holiday pay, sick pay, overtime, taxes, and insurance, are no longer your concern.</p>
<a class="btn btn-lg" style="left:379px;top:1039px">Learn More</a>
<a class="btn btn-lg" style="left:613px;top:1039px">Contact Us</a>

<section class="abs services"></section>
<h2 class="abs center services-title">SERVICES</h2>
<p class="abs services-text">Do you need some Smart Office Support (SOS)? Do you have a huge project looming on the horizon? Do you just need a little support managing the growing stacks of To-Dos cluttering your desk? As a master of managing the barrage of daily details that require concise and prompt attention, SOS is my speciality, from organisation to proofreading, no detail is too small!</p>

<div class="card" style="left:74px;top:1402px">
  <svg class="card-icon" viewBox="0 0 52 52"><path d="M12 4h20l10 10v34H12z" fill="#666"/><path d="M32 4v10h10" fill="#999"/><rect x="18" y="22" width="18" height="3" fill="#fff"/><rect x="18" y="29" width="18" height="3" fill="#fff"/><rect x="18" y="36" width="18" height="3" fill="#fff"/></svg>
  <div class="card-title">Organizational/Project Management</div>
  <div class="card-text">Reliable project and team management, master of organisation.</div>
  <a class="btn btn-sm" style="left:100px;top:128px">Learn More</a>
  <a class="btn btn-sm" style="left:282px;top:128px">Contact Us</a>
</div>
<div class="card" style="left:613px;top:1402px">
  <svg class="card-icon" viewBox="0 0 52 52"><rect x="8" y="4" width="36" height="44" rx="3" fill="none" stroke="#666" stroke-width="3"/><rect x="13" y="9" width="26" height="9" fill="#666"/><g fill="#666"><rect x="13" y="23" width="6" height="5"/><rect x="23" y="23" width="6" height="5"/><rect x="33" y="23" width="6" height="5"/><rect x="13" y="31" width="6" height="5"/><rect x="23" y="31" width="6" height="5"/><rect x="33" y="31" width="6" height="5"/><rect x="13" y="39" width="6" height="5"/><rect x="23" y="39" width="6" height="5"/><rect x="33" y="39" width="6" height="5"/></g></svg>
  <div class="card-title">Administrative and Accounting Support</div>
  <div class="card-text">Work smarter not harder with the right VA by your side.</div>
  <a class="btn btn-sm" style="left:100px;top:128px">Learn More</a>
  <a class="btn btn-sm" style="left:282px;top:128px">Contact Us</a>
</div>
<div class="card" style="left:74px;top:1638px">
  <svg class="card-icon" viewBox="0 0 52 52"><rect x="8" y="12" width="36" height="24" rx="2" fill="none" stroke="#666" stroke-width="3"/><path d="M2 40h48l-3 4H5z" fill="#666"/></svg>
  <div class="card-title">Website Administration</div>
  <div class="card-text">Dependable and reliable website updates--like clockwork.</div>
  <a class="btn btn-sm" style="left:100px;top:128px">Learn More</a>
  <a class="btn btn-sm" style="left:282px;top:128px">Contact Us</a>
</div>
<div class="card" style="left:613px;top:1638px">
  <svg class="card-icon" viewBox="0 0 52 52"><rect x="4" y="8" width="30" height="36" rx="2" fill="none" stroke="#666" stroke-width="3"/><path d="M9 16l3 3 5-6M9 28l3 3 5-6M9 38l6 0" stroke="#666" stroke-width="2.5" fill="none"/><circle cx="34" cy="30" r="9" fill="#fff" stroke="#666" stroke-width="3"/><path d="M41 37l8 8" stroke="#666" stroke-width="4"/></svg>
  <div class="card-title">Editorial Service/Proofreading</div>
  <div class="card-text">Catching simple typos and grammatical faux pas to preserve your integrity.</div>
  <a class="btn btn-sm" style="left:100px;top:128px">Learn More</a>
  <a class="btn btn-sm" style="left:282px;top:128px">Contact Us</a>
</div>

<p class="abs center tagline script">If you want something done right &nbsp; find the<br>right person to do it!</p>

<section class="abs why"></section>
<h2 class="abs why-title">WHY ME?</h2>
<p class="abs why-text">I offer administrative, management, and editorial services for those in need of an expert, professional, and discreet “virtual” assistant.<br>As an independent contractor, I can offer you these services with all the same dedication and loyalty as a full-time staff assistant --<br>at a more cost- effective rate.</p>
<div class="abs why-photo" role="img" aria-label="Portrait photo of the virtual assistant"></div>
<div class="abs caption-name">Maren T Holloway</div>
<div class="abs caption-role">VA &amp; Proofreader</div>

<div class="story-photo" style="left:74px;background:linear-gradient(120deg,#e4e2dc,#b9b2a6 50%,#7b8fa6)" role="img" aria-label="Photo of three colleagues reviewing documents at a desk"></div>
<h3 class="story-title" style="left:74px">Who’s benefited from my help...</h3>
<p class="story-text" style="left:74px">My employers and clients hail from backgrounds in marketing, education, import/export businesses, IT, health and wellbeing and hospitality.<br>They range from small to large businesses and individuals, all with a common issue.</p>
<div class="load-more" style="left:74px;top:3041px;width:513px"><span>Load More</span><span class="rule"></span></div>

<div class="story-photo" style="left:613px;background:linear-gradient(120deg,#5a4a3c,#b08f73 50%,#d8d2c9)" role="img" aria-label="Photo of two women working at a shop counter with a computer"></div>
<h3 class="story-title" style="left:613px">What I can do for you...</h3>
<p class="story-text" style="left:613px">Sales accounting, inventory control, social media management, general office support, marketing assistance, client or HR relations, project management, contract reviews, regulatory compliance documentation ... essentially any area of business.</p>
<div class="load-more" style="left:613px;top:3041px;width:513px"><span>Load More</span><span class="rule"></span></div>

<div class="abs calling-photo" role="img" aria-label="Photo of a smiling woman in glasses shaking hands in an office"></div>
<section class="abs calling"></section>
<h2 class="abs calling-title">SOMETIMES YOUR CALLING...<br>WELL, IT FINDS YOU!</h2>
<p class="abs calling-text">I have over 30-years experience rescuing countless businesses from backlogs of work or faulty practices, and I have helped launched almost as many new businesses by building a solid foundation on sound systems.<br>I have a history of arriving in just the right place at just the right time -- when businesses and professionals need me the most.</p>
<div class="load-more" style="left:613px;top:3426px;width:513px;color:#fff"><span>Load More</span><span class="rule" style="background:#a89c98"></span></div>

<h2 class="abs center section-title testi-title">TESTIMONIALS</h2>
<div class="testi" style="left:80px">
  <div class="testi-mark">”</div>
  <p class="testi-text">“ Nulla posuere suscipit neque metus neque, eleifend quis dignissim nec, dignissim sit amet massa. Vivamus nibh ex, mollis in porttitor eget, sollicitudin non tellus.”</p>
  <div class="testi-name">-Name Heading</div>
</div>
<div class="testi" style="left:441px">
  <div class="testi-mark">”</div>
  <p class="testi-text">“ Nulla posuere suscipit neque metus neque, eleifend quis dignissim nec, dignissim sit amet massa. Vivamus nibh ex, mollis in porttitor eget, sollicitudin non tellus.”</p>
  <div class="testi-name">-Name Heading</div>
</div>
<div class="testi" style="left:802px">
  <div class="testi-mark">”</div>
  <p class="testi-text">“ Nulla posuere suscipit neque metus neque, eleifend quis dignissim nec, dignissim sit amet massa. Vivamus nibh ex, mollis in porttitor eget, sollicitudin non tellus.”</p>
  <div class="testi-name">-Name Heading</div>
</div>

<footer class="abs site-footer"></footer>
<nav class="abs center footer-nav"><span>HOME</span><span>ABOUT</span><span>SERVICES</span><span>FEES</span><span>TESTIMONIALS</span><span>CONTACT</span></nav>
<div class="abs center copyright">Copyright © 2020, Company Name All Right reserved</div>
<div class="abs center social" aria-label="Social media links"><span></span><span></span><span></span><span></span><span></span></div>

</body>
</html>
```